Defend science flier

Put my name and text below on one side of flier, and place other text on other side. Try to keep file about 4 by 6 or 6 by 8 inches.

Target Market(s)

Community and retailers.

Industry/Entity Type

Retail and concerned community.

Font styles to use
Serif

Requirements
Must have
• Good, eye-catching titles. Be smaller format. Not 8 by 11
Nice to have
• Black and white text. Maybe bullets etc for organizion but no decorations.
Should not have
• Any decoration

```html
<!DOCTYPE html>
<html lang="en">
<head>
<meta charset="utf-8">
<title>Walter Brennholt, Ph.D. — Flier</title>
<link rel="stylesheet" href="https://fonts.googleapis.com/css2?family=Source+Serif+4:opsz,wght@8..60,300;8..60,400;8..60,600;8..60,700;8..60,800&display=swap">
<style>
  :root {
    --backdrop: #7a7a7a;
    --paper: #fdfdf3;
    --white: #ffffff;
    --ink: #111111;
    --gold: #ad8f4c;
    --gold-line: #9a7a3a;
    --band-text: #fbf7e8;
  }
  * { margin: 0; padding: 0; box-sizing: border-box; }
  html, body { width: 1200px; height: 904px; overflow: hidden; }
  body {
    background: var(--backdrop);
    position: relative;
    font-family: "Source Serif 4", Georgia, "Times New Roman", serif;
    color: var(--ink);
  }
  .panel {
    position: absolute;
    top: 133px;
    width: 494px;
    height: 659px;
    background: var(--paper);
  }
  .panel--front { left: 84px; }
  .panel--back { left: 623px; }

  .panel-content {
    position: absolute;
    left: 0; right: 0;
    text-align: center;
    display: flex;
    flex-direction: column;
  }

  .body-copy { font-weight: 300; font-size: 15px; line-height: 20px; padding: 0 20px; }

  /* Front */
  .front-header { top: 30px; }
  .name {
    font-weight: 800; font-size: 33px; line-height: 42px;
    letter-spacing: -0.3px;
  }
  .tagline {
    margin-top: 2px;
    font-weight: 600; font-size: 16px; line-height: 22px;
  }
  .front-intro { top: 160px; gap: 20px; }

  .quote-box {
    position: absolute; left: 26px; top: 366px;
    width: 441px; height: 197px;
    background: var(--white);
    border: 1px solid var(--gold-line);
    border-radius: 4px;
    display: flex;
    flex-direction: column;
    justify-content: center;
    gap: 12px;
    padding: 0 16px;
    text-align: center;
  }
  .quote-text { font-weight: 600; font-size: 13px; line-height: 17.5px; }
  .quote-credit { font-weight: 300; font-size: 11.5px; line-height: 15px; }

  .footer-band {
    position: absolute; left: 0; bottom: 0;
    width: 100%; height: 76px;
    background: var(--gold);
    color: var(--band-text);
    text-align: center;
  }
  .footer-cta {
    position: absolute; left: 0; right: 0; top: 16px;
    font-weight: 600; font-size: 16px; line-height: 20px; letter-spacing: 0.3px;
  }
  .footer-url {
    position: absolute; left: 0; right: 0; top: 38px;
    font-weight: 300; font-size: 15px; line-height: 20px;
  }

  /* Back */
  .sins-box {
    position: absolute; left: 26px; top: 25px;
    width: 441px; height: 310px;
    background: var(--white);
    border: 1px solid var(--gold-line);
    border-radius: 4px;
  }
  .sins-title {
    position: absolute; left: 0; right: 22px; top: 10px;
    text-align: center;
    font-weight: 700; font-size: 19px; line-height: 26px;
  }
  .sins-lead {
    position: absolute; left: 26px; right: 14px; top: 46px;
    font-weight: 600; font-size: 12.5px; line-height: 17px;
  }
  .sin-list { list-style: none; }
  .sin-item {
    position: absolute; left: 26px; right: 14px;
    display: flex; align-items: center;
    font-weight: 600; font-size: 12.5px; line-height: 16px;
  }
  .sin-number { flex: 0 0 34px; width: 34px; height: 34px; margin-right: 8px; }
  .sin-item--1 { top: 69px; }
  .sin-item--2 { top: 113px; }
  .sin-item--3 { top: 157px; }
  .sin-item--4 { top: 201px; }
  .sin-item--5 { top: 245px; }
  .sin-item--5 span { position: relative; top: 7px; }

  .back-copy { top: 352px; gap: 17px; }
  .back-copy .body-copy { font-size: 14px; line-height: 18.5px; }
</style>
</head>
<body>

<section class="panel panel--front">
  <header class="panel-content front-header">
    <h1 class="name">Walter Brennholt, Ph.D.</h1>
    <p class="tagline">“The Newton and Einstein of Psychology and History.”</p>
  </header>

  <div class="panel-content front-intro">
    <p class="body-copy">Walter’s Bio-Psych has Restructured the Liberal Arts and Sciences—from Genetics to the Fine Arts and Hollywood.</p>
    <p class="body-copy">Museum Catalogues, Better Nonfiction, and Hollywood Films Now Use Walter’s Methods.</p>
    <p class="body-copy">Walter’s Biopsych is endorsed by Dr. R. Milton Archer, professor of psychiatry at Eastbrook Medical School, who said:</p>
  </div>

  <blockquote class="quote-box">
    <p class="quote-text">“Modern sleep and dream research teaches us—as does Walter Brennholt’s book Private Sin or Public Sin—that all human activities, including art and politics, are products of the human brain, and that each of us has the privilege and responsibility of using it and communicating its creations.”</p>
    <p class="quote-credit">—Dr. R. Milton Archer, Professor of Psychiatry, Emeritus, Eastbrook Medical School, author of ‘Night Mind: An Introduction to the Science of Sleep’ (Halden University Press, 2004).</p>
  </blockquote>

  <footer class="footer-band">
    <p class="footer-cta">SEE WALTER’S HOMEPAGE FOR MORE DETAILS:</p>
    <p class="footer-url">www.walter-brennholt.org</p>
  </footer>
</section>

<section class="panel panel--back">
  <div class="sins-box">
    <h2 class="sins-title">Why Did the Culture Change?</h2>
    <p class="sins-lead">During the 1960s, we socialized the Seven Deadly Sins.Therefore:</p>
    <ol class="sin-list">
      <li class="sin-item sin-item--1">
        <svg class="sin-number" viewBox="0 0 34 34" aria-hidden="true"><circle cx="17" cy="17" r="17" fill="#ad8f4c"/><circle cx="17" cy="17" r="13.5" fill="none" stroke="#fff" stroke-width="1.6"/><text x="17" y="23.5" text-anchor="middle" font-family="Source Serif 4, Georgia, serif" font-size="19" fill="#fff">1</text></svg>
        <span>Pride became “Racism.”</span>
      </li>
      <li class="sin-item sin-item--2">
        <svg class="sin-number" viewBox="0 0 34 34" aria-hidden="true"><circle cx="17" cy="17" r="17" fill="#ad8f4c"/><circle cx="17" cy="17" r="13.5" fill="none" stroke="#fff" stroke-width="1.6"/><text x="17" y="23.5" text-anchor="middle" font-family="Source Serif 4, Georgia, serif" font-size="19" fill="#fff">2</text></svg>
        <span>Lust became “Sexism” and “Gender“ existing “out there.”</span>
      </li>
      <li class="sin-item sin-item--3">
        <svg class="sin-number" viewBox="0 0 34 34" aria-hidden="true"><circle cx="17" cy="17" r="17" fill="#ad8f4c"/><circle cx="17" cy="17" r="13.5" fill="none" stroke="#fff" stroke-width="1.6"/><text x="17" y="23.5" text-anchor="middle" font-family="Source Serif 4, Georgia, serif" font-size="19" fill="#fff">3</text></svg>
        <span>Gluttony became “Consumer Fetishism.”</span>
      </li>
      <li class="sin-item sin-item--4">
        <svg class="sin-number" viewBox="0 0 34 34" aria-hidden="true"><circle cx="17" cy="17" r="17" fill="#ad8f4c"/><circle cx="17" cy="17" r="13.5" fill="none" stroke="#fff" stroke-width="1.6"/><text x="17" y="23.5" text-anchor="middle" font-family="Source Serif 4, Georgia, serif" font-size="19" fill="#fff">4</text></svg>
        <span>Vanity became “Media Images of Beauty.”</span>
      </li>
      <li class="sin-item sin-item--5">
        <svg class="sin-number" viewBox="0 0 34 34" aria-hidden="true"><circle cx="17" cy="17" r="17" fill="#ad8f4c"/><circle cx="17" cy="17" r="13.5" fill="none" stroke="#fff" stroke-width="1.6"/><text x="17" y="23.5" text-anchor="middle" font-family="Source Serif 4, Georgia, serif" font-size="19" fill="#fff">5</text></svg>
        <span>Sloth became The lack of social action: “Are you fighting for diversity?”</span>
      </li>
    </ol>
  </div>

  <div class="panel-content back-copy">
    <p class="body-copy">This “fight for diversity” inspires attacks against people like Dr. Brennholt for asserting any reality principle about human nature.</p>
    <p class="body-copy">These thugs are religious crusaders who ignore the rule of law and try to stop the progress of science. These fanatics goaround and givepeople a “tear-test”—as during the Salem witch trials. Don’t let them take over.</p>
    <p class="body-copy">The educational and culture elites—such as Hollywood—now reject these theological “social sins.” The elites are replacing theology with traditional, human-based sin.</p>
  </div>

  <footer class="footer-band">
    <p class="footer-cta">SEE WALTER’S HOMEPAGE FOR MORE DETAILS:</p>
    <p class="footer-url">www.walter-brennholt.org</p>
  </footer>
</section>

</body>
</html>
```